Price Calculator as Responsive Web App to support Sales People

We need to build a simple micro web app to support sales people in making quotes. We already have a backend that can take a number of parameters and create a quote. We need put a responsive web app on top of this so that our people on the road can easily do their price simulations.

We need two pages. One for the input and another for the results. No menus, navigations, etc. It is 6 different inputs as shown with boxes in the sketch. They don't need to be boxed, but some of them have a bit of instruction text that clearly need to belong to the input.

This needs to be responsive, but first and foremost designed for smartphones. I have included a background gradient that we would like to use -- or a variant of it. We expect this to be delivered as HTML/CSS + images so that we can quickly write a few pieces of JavaScript ourselves to wire it up to our price simulator.

Industry/Entity Type

Information Technology

Coding

Coded - Design and coding required

Number of Pages Required

2 page

Font styles to use
Sans Serif

Requirements
Must have
• Responsive design
• Easy to wire up JavaScript to the HTML/CSS
Nice to have
• Some quick way to pick number of months. +/- buttons to add remove a year or 3 months. Same thing with number of items. Add 10 or 5 quickly.
• Maybe some parallax effect while scrolling as long as it is not distracting.
Should not have
• Toolbars, Menus, Navigations, Banners, etc. This is just a single micro app.

```html
<!DOCTYPE html>
<html lang="en">
<head>
<meta charset="UTF-8">
<title>Price Calculator – Results</title>
<link href="https://fonts.googleapis.com/css2?family=Nunito:wght@400;500&display=swap" rel="stylesheet">
<style>
  :root {
    --bg-top: #011a31;
    --bg-bottom: #04386a;
    --card: #ebecee;
    --header: #022c4f;
    --row-alt: #e8ebee;
    --row: #ffffff;
    --ink: #0b2c4c;
    --divider: #c9cdd2;
    --total: #6ecdef;
    --cap: #e23b3b;
    --axis: #6b6b6b;
  }
  * { box-sizing: border-box; margin: 0; padding: 0; }
  html, body { width: 994px; height: 1200px; overflow: hidden; }
  body {
    position: relative;
    font-family: "Nunito", sans-serif;
    background: linear-gradient(180deg, var(--bg-top) 0%, var(--bg-bottom) 100%);
    color: var(--ink);
  }
  .results-card {
    position: absolute;
    left: 36px; top: 36px;
    width: 921px; height: 1164px;
    background: var(--card);
    border-radius: 6px 6px 0 0;
  }
  .quote-table {
    position: absolute;
    left: 26px; top: 26px;
    width: 869px;
    border-collapse: collapse;
    border: 1px solid var(--divider);
  }
  .quote-table th, .quote-table td {
    height: 80px;
    text-align: left;
    font-weight: 400;
    font-size: 29px;
    vertical-align: middle;
  }
  .quote-table col.label { width: 297px; }
  .quote-table col.month { width: 293px; }
  .quote-table col.year  { width: 279px; }
  .quote-table th {
    background: var(--header);
    color: #ffffff;
    font-size: 24px;
    text-align: center;
  }
  .quote-table td { padding-left: 52px; }
  .quote-table td.month { padding-left: 104px; }
  .quote-table td.year  { padding-left: 86px; }
  .quote-table td + td { border-left: 1px solid var(--divider); }
  .quote-table tbody tr:nth-child(odd)  { background: var(--row-alt); }
  .quote-table tbody tr:nth-child(even) { background: var(--row); }
  .quote-table tr.total-row { color: var(--total); }
  .quote-table tr.cap-row td { color: var(--cap); height: 88px; }
  .comparison-chart {
    position: absolute;
    left: 0; top: 0;
  }
  .chart-label {
    font-family: "Nunito", sans-serif;
    font-size: 21px;
    fill: var(--total);
  }
</style>
</head>
<body>
  <main class="results-card">
    <table class="quote-table">
      <colgroup><col class="label"><col class="month"><col class="year"></colgroup>
      <thead>
        <tr><th></th><th>Per/Month</th><th>Per/Year</th></tr>
      </thead>
      <tbody>
        <tr><td>Items</td><td class="month">350</td><td class="year">4200</td></tr>
        <tr><td>Engine</td><td class="month">250</td><td class="year">3000</td></tr>
        <tr><td>Storage</td><td class="month">200</td><td class="year">2400</td></tr>
        <tr><td>Tip</td><td class="month">52</td><td class="year">630</td></tr>
        <tr class="total-row"><td>Total</td><td class="month">852</td><td class="year">10230</td></tr>
        <tr class="cap-row"><td>Cap</td><td class="month">1278</td><td class="year">15345</td></tr>
      </tbody>
    </table>
  </main>

  <svg class="comparison-chart" width="994" height="1200" viewBox="0 0 994 1200" aria-label="Total versus cap bar chart">
    <g stroke="var(--axis)" stroke-width="2.5" fill="none">
      <line x1="300" y1="738" x2="300" y2="1045"/>
      <line x1="299" y1="1044" x2="696" y2="1044"/>
      <line x1="282" y1="763" x2="300" y2="763"/>
      <line x1="282" y1="863" x2="300" y2="863"/>
      <line x1="282" y1="950" x2="300" y2="950"/>
    </g>
    <g fill="var(--total)">
      <rect x="338" y="762" width="91" height="88"/>
      <rect x="338" y="857" width="91" height="88"/>
      <rect x="338" y="953" width="91" height="88"/>
    </g>
    <g fill="var(--cap)">
      <rect x="449" y="857" width="91" height="88"/>
      <rect x="449" y="953" width="91" height="88"/>
    </g>
    <text class="chart-label" x="387" y="1087" text-anchor="middle">Total</text>
    <text class="chart-label" x="499" y="1087" text-anchor="middle">Cap</text>
  </svg>
</body>
</html>
```